Designer Instructions – Updated Referral Program Flyer

(Based on the mock-up in “Brief Layout and Instructions.pdf”)

OVERALL STYLE + LAYOUT

Maintain the same general layout, structure, and flow as the mock-up flyer (front and back).

This is an update of an older flyer, not a full redesign — keep the same sections, proportions, and overall visual feel, but with cleaner, more modern design improvements.

The final flyer should look clean, bold, professional, and high-impact, geared toward realtors, property managers, and contractors who refer work.

FRONT SIDE INSTRUCTIONS
1. Header Section

Remove the Tallow Ridge Builders logo from the top banner.
(Shown on page 1 of the PDF)

2. Main Headline

Keep the same three-line structure:
EARN
UNLIMITED
CASH

Center it, maximize impact, and increase the font size of CASH so all three words match in importance.

Make the headline bold, clean, and the main focal point.

3. Cash Incentive Box

Keep the "$500 minimum OR 10% per referral" box, but upgrade the graphics to look sharper and more modern.

Ensure the wording matches exactly what’s in the mock-up.

4. Premier Partner Program Ribbon

Clean up and modernize the "PREMIER PARTNER PROGRAM" bar while keeping the same position and structure.

Ensure the checkmark badge remains crisp and professional.

5. Supporting Icons Section

Keep the four icons/benefit boxes (Guaranteed Payout, Free Evaluations, Affordable Solutions, Industry Leaders) in the same order.

Update the icons to cleaner, more modern styles — but maintain the same meanings.

Improve alignment and spacing for sharper visual consistency.

6. Remove Icons in Contact Area

At the bottom (“CALL TEXT OR BOOK ONLINE 555-014-2796 TallowRidgeBuilders.example”), remove the phone and internet icons, as noted on page 2 of the PDF.

7. Replace All Images

I (Darnell) will provide all updated stock images separately via email.

Replace the flood/water-damage imagery and roof leak with the new images I send.

Keep image placement and proportions the same as the mock-up.

BACK SIDE INSTRUCTIONS
1. Header Image + “REFER / EARN” Section

Maintain the same large split-image layout (“The more you refer, the more you earn”).

Replace all background imagery with the new assets I will send.

Keep the CASH FLOW image section but modernize the type and spacing.

2. “HOW IT WORKS” Section

Preserve the three-column layout:

Refer Flood, Water & Mold Damage

We Take Care of Everything (evaluations/insurance)

Get Paid to Share

Update images, tighten spacing, and use modern iconography.

3. Remove Phone/Internet Icons

Same as the front side — remove small communication icons and keep only the text/number/URL.

4. Bottom Contact Bar

Keep the blue bar, same wording, same layout — just modernize the style if needed for clarity.

5. Replace All Back-Side Images

Again, I will email you the image assets.

Keep the layout EXACT — just update with higher-quality photos and improved design.

TEXT CONTENT (Keep as-is unless spacing adjustments needed)

All text shown in the PDF should remain exactly the same unless spacing or visual balance requires minor adjustments.
Example from page 3:

“REFER FLOOD, MOLD & CONSTRUCTION JOBS”

“We Schedule a Free Estimate. If Approved, You Get Paid.”

“Everybody Benefits From Referrals”

Everything stays, just refreshed and visually improved.

DESIGN GOALS

Flyer should look high-end and trustworthy, not salesy.

Consistent color theme: blues, whites, yellows, same palette as original.

Use bold, modern fonts with strong readability.

Ensure all headlines pop and all benefit boxes are clean, well-aligned, and evenly spaced.

The final result should feel like a premium referral program flyer for a top-tier restoration/remodel company.

FILES I WILL PROVIDE

I will send the designer:

All replacement stock photos

Any updated logos (if needed)

Original high-resolution version of the mock-up (if available)

Any additional icons preferred

0054AA
0677BA
7BADD7
CADEEF
E8F1F8

• Designer Instructions – Updated Referral Program Flyer (Based on the mock-up in “Brief Layout and Instructions.pdf”) OVERALL STYLE + LAYOUT Maintain the same general layout, structure, and flow as the mock-up flyer (front and back). This is an update of an older flyer, not a full redesign — keep the same sections, proportions, and overall visual feel, but with cleaner, more modern design improvements. The final flyer should look clean, bold, professional, and high-impact, geared toward realtors, property managers, and contractors who refer work. FRONT SIDE INSTRUCTIONS 1. Header Section Remove the Tallow Ridge Builders logo from the top banner. (Shown on page 1 of the PDF) 2. Main Headline Keep the same three-line structure: EARN UNLIMITED CASH Center it, maximize impact, and increase the font size of CASH so all three words match in importance. Make the headline bold, clean, and the main focal point. 3. Cash Incentive Box Keep the "$500 minimum OR 10% per referral" box, but upgrade the graphics to look sharper and more modern. Ensure the wording matches exactly what’s in the mock-up. 4. Premier Partner Program Ribbon Clean up and modernize the "PREMIER PARTNER PROGRAM" bar while keeping the same position and structure. Ensure the checkmark badge remains crisp and professional. 5. Supporting Icons Section Keep the four icons/benefit boxes (Guaranteed Payout, Free Evaluations, Affordable Solutions, Industry Leaders) in the same order. Update the icons to cleaner, more modern styles — but maintain the same meanings. Improve alignment and spacing for sharper visual consistency. 6. Remove Icons in Contact Area At the bottom (“CALL TEXT OR BOOK ONLINE 555-014-2796 TallowRidgeBuilders.example”), remove the phone and internet icons, as noted on page 2 of the PDF. 7. Replace All Images I (Darnell) will provide all updated stock images separately via email. Replace the flood/water-damage imagery and roof leak with the new images I send. Keep image placement and proportions the same as the mock-up. BACK SIDE INSTRUCTIONS 1. Header Image + “REFER / EARN” Section Maintain the same large split-image layout (“The more you refer, the more you earn”). Replace all background imagery with the new assets I will send. Keep the CASH FLOW image section but modernize the type and spacing. 2. “HOW IT WORKS” Section Preserve the three-column layout: Refer Flood, Water & Mold Damage We Take Care of Everything (evaluations/insurance) Get Paid to Share Update images, tighten spacing, and use modern iconography. 3. Remove Phone/Internet Icons Same as the front side — remove small communication icons and keep only the text/number/URL. 4. Bottom Contact Bar Keep the blue bar, same wording, same layout — just modernize the style if needed for clarity. 5. Replace All Back-Side Images Again, I will email you the image assets. Keep the layout EXACT — just update with higher-quality photos and improved design. TEXT CONTENT (Keep as-is unless spacing adjustments needed) All text shown in the PDF should remain exactly the same unless spacing or visual balance requires minor adjustments. Example from page 3: “REFER FLOOD, MOLD & CONSTRUCTION JOBS” “We Schedule a Free Estimate. If Approved, You Get Paid.” “Everybody Benefits From Referrals” Everything stays, just refreshed and visually improved. DESIGN GOALS Flyer should look high-end and trustworthy, not salesy. Consistent color theme: blues, whites, yellows, same palette as original. Use bold, modern fonts with strong readability. Ensure all headlines pop and all benefit boxes are clean, well-aligned, and evenly spaced. The final result should feel like a premium referral program flyer for a top-tier restoration/remodel company. FILES I WILL PROVIDE I will send the designer: All replacement stock photos Any updated logos (if needed) Original high-resolution version of the mock-up (if available) Any additional icons preferred

```html
<!DOCTYPE html>
<html lang="en">
<head>
<meta charset="utf-8">
<title>Referral Program – How It Works</title>
<link href="https://fonts.googleapis.com/css2?family=Archivo+Black&family=Montserrat:wght@600;700;800;900&display=swap" rel="stylesheet">
<style>
  :root {
    --banner-blue: #176aa0;
    --banner-navy: #06273d;
    --strip-yellow: #fbd500;
    --ink-navy: #1e3278;
    --tile-blue: #0f5b8f;
    --tile-edge: #0a3f66;
    --card-border: #1d2f73;
    --bar-navy: #183273;
    --white: #ffffff;
    --steel: #9da3a8;
  }
  * { box-sizing: border-box; margin: 0; padding: 0; }
  html, body { width: 1200px; height: 800px; overflow: hidden; background: var(--white); }
  .flyer { position: relative; width: 1200px; height: 800px; background: var(--white); font-family: "Montserrat", sans-serif; }

  .hero { position: absolute; left: 0; top: 0; width: 1200px; height: 360px; }
  .hero svg { position: absolute; left: 0; top: 0; }

  .cash-tiles { position: absolute; left: 786px; width: 254px; display: flex; gap: 2px; }
  .cash-tiles.row-one { top: 103px; }
  .cash-tiles.row-two { top: 187px; }
  .tile {
    flex: 1; height: 63px; background: var(--tile-blue);
    border: 2px solid var(--tile-edge); border-radius: 3px;
    color: var(--white); font-weight: 800; font-size: 56px; line-height: 59px; text-align: center;
    box-shadow: 0 2px 4px rgba(0,0,0,.35);
  }

  .how-title {
    position: absolute; left: 120px; top: 292px;
    font-family: "Montserrat", sans-serif; font-weight: 800; font-size: 49px; letter-spacing: -1px;
    color: var(--ink-navy); line-height: 54px;
  }

  .steps { position: absolute; top: 372px; left: 93px; width: 1020px; height: 312px; }
  .step {
    position: absolute; top: 0; width: 325px; height: 312px;
    border: 5px solid var(--card-border); border-radius: 30px; overflow: hidden;
    background: linear-gradient(100deg, #a9aeb3 0%, #e4e6e8 45%, #ffffff 80%, #f2f3f4 100%);
  }
  .step:nth-child(1) { left: 0; }
  .step:nth-child(2) { left: 348px; }
  .step:nth-child(3) { left: 695px; }
  .step-photo { height: 174px; width: 100%; }
  .photo-drying { background: linear-gradient(160deg, #d9d6cf 0%, #bfc3c2 40%, #4aa3cf 70%, #2f86b8 100%); }
  .photo-estimate { background: linear-gradient(180deg, #c9c4bd 0%, #eeeeea 40%, #7a9a5b 75%, #7fb2d9 100%); }
  .photo-sign { background: linear-gradient(135deg, #5a93d6 0%, #cfe1f3 45%, #f4e23a 65%, #8db8e6 100%); }
  .step-text { padding: 10px 6px 0; text-align: center; color: var(--ink-navy); }
  .step-title { font-weight: 900; font-size: 20.5px; line-height: 22px; letter-spacing: .2px; }
  .step-body { font-weight: 600; font-size: 18.5px; line-height: 20.5px; letter-spacing: .3px; }
  .step:nth-child(3) .step-body { line-height: 27.5px; margin-top: 4px; }

  .contact-bar { position: absolute; left: 0; top: 709px; }
  .contact-label {
    position: absolute; left: 93px; top: 722px;
    color: var(--white); font-weight: 800; font-size: 25.5px; letter-spacing: .6px; line-height: 30px;
  }
  .contact-label .soft { font-weight: 600; }
  .contact-details {
    position: absolute; left: 538px; top: 721px;
    color: var(--ink-navy); font-weight: 700; font-size: 25px; line-height: 30px; letter-spacing: -.3px;
  }
</style>
</head>
<body>
<main class="flyer">

  <section class="hero">
    <svg width="1200" height="360" viewBox="0 0 1200 360">
      <defs>
        <linearGradient id="goldFill" x1="0" y1="0" x2="1" y2="1">
          <stop offset="0" stop-color="#f7ee3a"/>
          <stop offset=".5" stop-color="#f6c22a"/>
          <stop offset="1" stop-color="#f1913e"/>
        </linearGradient>
        <linearGradient id="cashBg" x1="0" y1="0" x2="1" y2="1">
          <stop offset="0" stop-color="#d8d6dc"/>
          <stop offset=".5" stop-color="#eeeef0"/>
          <stop offset="1" stop-color="#b9b8c0"/>
        </linearGradient>
      </defs>
      <rect class="banner-field" x="17" y="17" width="620" height="332" fill="var(--banner-blue)"/>
      <polygon class="banner-shadow" points="119,61 628,97 679,290 215,290 119,261" fill="var(--banner-navy)"/>
      <polygon class="cash-photo" role="img" aria-label="Photo of scattered hundred-dollar bills" points="625,17 1184,17 1184,349 712,349" fill="url(#cashBg)"/>
      <polygon class="divider-stripe" points="607,17 625,17 712,349 694,349" fill="var(--steel)"/>
      <polygon class="how-strip" points="17,290 679,290 695,349 17,349" fill="var(--strip-yellow)"/>

      <text x="119" y="89" textLength="382" lengthAdjust="spacingAndGlyphs" font-family="Archivo Black, sans-serif" font-size="39" fill="#fff">THE MORE YOU</text>
      <text x="118" y="154" textLength="384" lengthAdjust="spacingAndGlyphs" font-family="Archivo Black, sans-serif" font-size="87" fill="url(#goldFill)">REFER</text>
      <text x="119" y="185" textLength="382" lengthAdjust="spacingAndGlyphs" font-family="Archivo Black, sans-serif" font-size="39" fill="#fff">THE MORE YOU</text>
      <text x="119" y="262" textLength="383" lengthAdjust="spacingAndGlyphs" font-family="Archivo Black, sans-serif" font-size="102" fill="url(#goldFill)">EARN</text>
    </svg>

    <div class="cash-tiles row-one"><span class="tile">C</span><span class="tile">A</span><span class="tile">S</span><span class="tile">H</span></div>
    <div class="cash-tiles row-two"><span class="tile">F</span><span class="tile">L</span><span class="tile">O</span><span class="tile">W</span></div>

    <h2 class="how-title">HOW IT WORKS</h2>
  </section>

  <section class="steps">
    <article class="step">
      <div class="step-photo photo-drying" role="img" aria-label="Photo of air movers and dehumidifiers drying a flooded room"></div>
      <div class="step-text">
        <h3 class="step-title">REFER FLOOD, WATER<br>AND MOLD DAMAGE</h3>
        <p class="step-body">Our Rapid 24/7 Response<br>Team Arrives Fast to<br>Stop the Damage</p>
      </div>
    </article>
    <article class="step">
      <div class="step-photo photo-estimate" role="img" aria-label="Photo of an inspector holding a work estimate in front of a house"></div>
      <div class="step-text">
        <h3 class="step-title">WE TAKE CARE OF<br>EVERYTHING</h3>
        <p class="step-body">Free Inspection and Estimates<br>Certified Repairs<br>100% Guarantee</p>
      </div>
    </article>
    <article class="step">
      <div class="step-photo photo-sign" role="img" aria-label="Photo of a yellow road sign reading Get Paid to Share against a cloudy sky"></div>
      <div class="step-text">
        <h3 class="step-title">GET PAID TO SHARE</h3>
        <p class="step-body">You Get Paid and Your Client<br>Gets The Help They<br>Need Fast</p>
      </div>
    </article>
  </section>

  <svg class="contact-bar" width="560" height="80" viewBox="0 0 560 80">
    <polygon points="17,0 510,0 552,74 17,74" fill="var(--bar-navy)"/>
  </svg>
  <p class="contact-label">CALL, TEXT <span class="soft">OR</span> BOOK ONLINE</p>
  <p class="contact-details">555-014-2796 • TallowRidgeBuilders.example</p>

</main>
</body>
</html>
```